KEV.PRO- Darren Holcombe Fitness- needs a clever business card using the logo, name, info, contact

I need a business card designed for my Online Personal Training company called KEV.PRO, abbreviation for Darren Holcombe Fitness. My company focuses on coaching in personal health and personal growth to unleash your greatest potential. I would like to see designs that use my color scheme of a redish-orange (C:0,M:84,Y:100,K:0), grey, white, black, and my company font is OSWALD. The final design should communicate some aspects of design, health, motivation, growth, in some way. The logo is very important to the company and can be displayed in any of the colors previously mentioned. Must include the company name, my website: www.kev-pro.example , my email: dan@kev-pro.example

Target Market(s)

Personal health, fitness, general public, those who lack knowledge, awareness, and confidence in personal health

Industry/Entity Type

Personal Trainer

Font styles to use
Other font styles liked:
• OSWALD. (Bold, Regular, Light)

Colors
f37122
ffffff
9d9d9d
000000

Requirements
Must have
• Must include the logo, company name, my website: www.kev-pro.example , my email: dan@kev-pro.example
Nice to have
• Variations of the colors scheme of a redish-orange (C:0,M:84,Y:100,K:0), grey, white, black. Logo, card, or text can be in any of these colors.
• Possible quote like "Take control of your personal health to unleash your greatest potential" or "Unleashing your greatness first begins with fitness of the body and mind"

```html
<!DOCTYPE html>
<html lang="en">
<head>
<meta charset="utf-8">
<title>KEV.PRO Business Card</title>
<link rel="stylesheet" href="https://fonts.googleapis.com/css2?family=Oswald:wght@300;400;700&display=swap">
<style>
  :root {
    --brand-orange: #f04e23;
    --brand-orange-light: #f57a45;
    --card-dark: #2b2b2b;
    --card-white: #ffffff;
    --ink-black: #1a1a1a;
    --stage: #e9e9ea;
  }
  html, body {
    margin: 0;
    padding: 0;
    width: 1200px;
    height: 863px;
    overflow: hidden;
    background: var(--stage);
    font-family: "Oswald", sans-serif;
  }
  .canvas {
    width: 1200px;
    height: 863px;
    display: flex;
    align-items: center;
    justify-content: center;
    gap: 60px;
  }
  .card {
    width: 330px;
    height: 560px;
    position: relative;
    overflow: hidden;
    box-shadow: 0 6px 24px rgba(0,0,0,0.12);
  }

  /* Contact side */
  .card--front {
    background: var(--card-dark);
  }
  .front-header {
    position: absolute;
    top: 0;
    left: 0;
    width: 330px;
    height: 260px;
    display: block;
  }
  .front-header__band { fill: var(--card-white); }
  .front-header__rule {
    fill: none;
    stroke: var(--brand-orange);
    stroke-width: 2;
  }
  .contact {
    position: absolute;
    left: 46px;
    top: 300px;
    color: var(--card-white);
  }
  .contact__name {
    margin: 0;
    font-weight: 700;
    font-size: 24px;
    letter-spacing: 0.5px;
    color: var(--brand-orange);
    line-height: 1.2;
    text-transform: uppercase;
  }
  .contact__role {
    margin: 2px 0 26px;
    font-weight: 300;
    font-size: 18px;
    text-transform: uppercase;
  }
  .contact__line {
    margin: 0;
    font-weight: 300;
    font-size: 17px;
    line-height: 1.3;
    text-transform: uppercase;
  }

  /* Brand side */
  .card--back {
    background: var(--card-white);
    display: flex;
    flex-direction: column;
    align-items: center;
    justify-content: center;
  }
  .brand-dot {
    width: 130px;
    height: 130px;
    border-radius: 50%;
    background: var(--brand-orange);
    margin-bottom: 20px;
  }
  .brand-name {
    margin: 0;
    font-weight: 700;
    font-size: 46px;
    line-height: 1;
    color: var(--ink-black);
  }
  .brand-tagline {
    margin: 6px 0 0;
    font-weight: 400;
    font-size: 12px;
    color: var(--ink-black);
    text-transform: uppercase;
  }
</style>
</head>
<body>
  <main class="canvas">
    <section class="card card--front">
      <svg class="front-header" viewBox="0 0 330 260" role="img" aria-label="Large cropped brand symbol in orange and white above a curved white band">
        <defs>
          <linearGradient id="header-fill" x1="0" y1="0" x2="1" y2="1">
            <stop offset="0" stop-color="var(--brand-orange)"/>
            <stop offset="1" stop-color="var(--brand-orange-light)"/>
          </linearGradient>
        </defs>
        <path class="front-header__band" d="M0,0 H330 V175 Q165,300 0,175 Z"/>
        <path d="M0,0 H330 V150 Q165,265 0,150 Z" fill="url(#header-fill)"/>
        <path class="front-header__rule" d="M0,165 Q165,285 330,165"/>
      </svg>
      <div class="contact">
        <h1 class="contact__name">Darren Holcombe</h1>
        <p class="contact__role">Owner</p>
        <p class="contact__line">www.kev-pro.example</p>
        <p class="contact__line">dan@kev-pro.example</p>
      </div>
    </section>
    <section class="card card--back">
      <div class="brand-dot" aria-hidden="true"></div>
      <h2 class="brand-name">KEV.PRO</h2>
      <p class="brand-tagline">Darren Holcombe Fitness</p>
    </section>
  </main>
</body>
</html>
```